Stationary and Business card design for a residential window and door manufacturing company
residential window and door manufacturing company
Simple
Tom Ashdale
General Manager
3870 Pellham Ridge Rd Toronto, ON M8K 2T6
t.ashdale@solvarowindowsanddoors.com
solvarowindowsanddoors.com
Side ways logo

```html
<!DOCTYPE html>
<html lang="en">
<head>
<meta charset="utf-8">
<title>Solvaro – Business Cards</title>
<link href="https://fonts.googleapis.com/css2?family=Montserrat:wght@700;800&family=Roboto:wght@400;500&display=swap" rel="stylesheet">
<style>
  :root{
    --backdrop:#d9d9db;
    --red:#e8232b;
    --black:#111111;
    --white:#ffffff;
    --ink:#1b1b1b;
  }
  *{margin:0;padding:0;box-sizing:border-box}
  html,body{width:1200px;height:849px;overflow:hidden;background:var(--backdrop)}
  .canvas{position:relative;width:1200px;height:849px}
  .card{position:absolute;left:367px;width:492px;height:235px;overflow:hidden;font-family:"Roboto",Arial,sans-serif}
  .card--light{top:168px;background:var(--white);color:var(--ink)}
  .card--red{top:480px;background:var(--red);color:var(--white)}
  .card__edges{position:absolute;inset:0;width:100%;height:100%}
  .brand{position:absolute;left:36px;top:64px;width:134px;display:flex;flex-direction:column;align-items:center;gap:10px}
  .brand__mark{width:40px;height:40px;background:var(--red)}
  .card--red .brand__mark{background:var(--white)}
  .brand__name{font-family:"Montserrat",Arial,sans-serif;font-weight:800;font-size:21px;line-height:1;letter-spacing:.3px;color:var(--red);text-transform:uppercase}
  .card--red .brand__name{color:var(--white)}
  .details{position:absolute;left:192px;top:18px;right:24px}
  .details__name{font-family:"Montserrat",Arial,sans-serif;font-weight:700;font-size:22px;line-height:1;color:var(--red);text-transform:uppercase;letter-spacing:-.3px}
  .card--red .details__name{color:var(--white)}
  .details__title{font-family:"Montserrat",Arial,sans-serif;font-weight:700;font-size:10.5px;margin-top:4px;text-transform:uppercase}
  .contact{list-style:none;margin-top:14px}
  .contact__row{display:flex;align-items:center;gap:9px;margin-bottom:11px}
  .contact__icon{width:22px;height:22px;flex:none}
  .contact__text{font-size:10px;line-height:1.45;font-weight:500;white-space:nowrap}
  .icon-bg{fill:var(--red)}
  .icon-fg{fill:var(--white)}
  .card--red .icon-bg{fill:var(--white)}
  .card--red .icon-fg{fill:var(--red)}
</style>
</head>
<body>
<main class="canvas">

  <section class="card card--light">
    <svg class="card__edges" viewBox="0 0 492 235" preserveAspectRatio="none" aria-hidden="true">
      <polygon points="0,30 28,92 20,235 0,235" fill="var(--black)"/>
      <polygon points="492,30 464,92 472,235 492,235" fill="var(--black)"/>
    </svg>
    <div class="brand"><span class="brand__mark"></span><span class="brand__name">Solvaro</span></div>
    <div class="details">
      <h1 class="details__name">Tom Ashdale</h1>
      <p class="details__title">General Manager</p>
      <ul class="contact">
        <li class="contact__row">
          <svg class="contact__icon" viewBox="0 0 24 24" aria-hidden="true"><circle class="icon-bg" cx="12" cy="12" r="12"/><path class="icon-fg" d="M12 5a4.5 4.5 0 0 0-4.5 4.5c0 3.2 4.5 9 4.5 9s4.5-5.8 4.5-9A4.5 4.5 0 0 0 12 5zm0 6.3a1.8 1.8 0 1 1 0-3.6 1.8 1.8 0 0 1 0 3.6z"/></svg>
          <p class="contact__text">3870 Pellham Ridge Rd<br>Toronto, ON<br>M8K 2T6</p>
        </li>
        <li class="contact__row">
          <svg class="contact__icon" viewBox="0 0 24 24" aria-hidden="true"><circle class="icon-bg" cx="12" cy="12" r="12"/><path class="icon-fg" d="M8.6 6.5l1.8-.4 1.2 3-1.3 1a8 8 0 0 0 3.6 3.6l1-1.3 3 1.2-.4 1.8c-.2.6-.8 1-1.4.9A10.5 10.5 0 0 1 7.6 7.9c-.1-.6.3-1.2 1-1.4z"/></svg>
          <p class="contact__text">905.555.0148<br>416.555.0193</p>
        </li>
        <li class="contact__row">
          <svg class="contact__icon" viewBox="0 0 24 24" aria-hidden="true"><circle class="icon-bg" cx="12" cy="12" r="12"/><path class="icon-fg" d="M12 5.5a6.5 6.5 0 1 0 0 13 6.5 6.5 0 0 0 0-13zm4.4 4h-2a10 10 0 0 0-.9-2.6 5 5 0 0 1 2.9 2.6zM12 7c.5.7.9 1.6 1.1 2.5h-2.2C11.1 8.6 11.5 7.7 12 7zm-4.3 6.2a5 5 0 0 1 0-2.4h2.1a11 11 0 0 0 0 2.4zm.3 1.3h2a10 10 0 0 0 .9 2.6 5 5 0 0 1-2.9-2.6zm2-5h-2a5 5 0 0 1 2.9-2.6c-.4.8-.7 1.7-.9 2.6zm2 7.5c-.5-.7-.9-1.6-1.1-2.5h2.2c-.2.9-.6 1.8-1.1 2.5zm1.4-3.8h-2.8a9 9 0 0 1 0-2.4h2.8a9 9 0 0 1 0 2.4zm.2 3.5c.4-.8.7-1.7.9-2.6h2a5 5 0 0 1-2.9 2.6zm1.1-3.8a11 11 0 0 0 0-2.4h2.1a5 5 0 0 1 0 2.4z"/></svg>
          <p class="contact__text">t.ashdale@solvarowindowsanddoors.com<br>solvarowindowsanddoors.com</p>
        </li>
      </ul>
    </div>
  </section>

  <section class="card card--red">
    <svg class="card__edges" viewBox="0 0 492 235" preserveAspectRatio="none" aria-hidden="true">
      <polygon points="0,30 28,92 20,235 0,235" fill="var(--black)"/>
      <polygon points="492,30 464,92 472,235 492,235" fill="var(--black)"/>
    </svg>
    <div class="brand"><span class="brand__mark"></span><span class="brand__name">Solvaro</span></div>
    <div class="details">
      <h2 class="details__name">Tom Ashdale</h2>
      <p class="details__title">General Manager</p>
      <ul class="contact">
        <li class="contact__row">
          <svg class="contact__icon" viewBox="0 0 24 24" aria-hidden="true"><circle class="icon-bg" cx="12" cy="12" r="12"/><path class="icon-fg" d="M12 5a4.5 4.5 0 0 0-4.5 4.5c0 3.2 4.5 9 4.5 9s4.5-5.8 4.5-9A4.5 4.5 0 0 0 12 5zm0 6.3a1.8 1.8 0 1 1 0-3.6 1.8 1.8 0 0 1 0 3.6z"/></svg>
          <p class="contact__text">3870 Pellham Ridge Rd<br>Toronto, ON<br>M8K 2T6</p>
        </li>
        <li class="contact__row">
          <svg class="contact__icon" viewBox="0 0 24 24" aria-hidden="true"><circle class="icon-bg" cx="12" cy="12" r="12"/><path class="icon-fg" d="M8.6 6.5l1.8-.4 1.2 3-1.3 1a8 8 0 0 0 3.6 3.6l1-1.3 3 1.2-.4 1.8c-.2.6-.8 1-1.4.9A10.5 10.5 0 0 1 7.6 7.9c-.1-.6.3-1.2 1-1.4z"/></svg>
          <p class="contact__text">905.555.0148<br>416.555.0193</p>
        </li>
        <li class="contact__row">
          <svg class="contact__icon" viewBox="0 0 24 24" aria-hidden="true"><circle class="icon-bg" cx="12" cy="12" r="12"/><path class="icon-fg" d="M12 5.5a6.5 6.5 0 1 0 0 13 6.5 6.5 0 0 0 0-13zm4.4 4h-2a10 10 0 0 0-.9-2.6 5 5 0 0 1 2.9 2.6zM12 7c.5.7.9 1.6 1.1 2.5h-2.2C11.1 8.6 11.5 7.7 12 7zm-4.3 6.2a5 5 0 0 1 0-2.4h2.1a11 11 0 0 0 0 2.4zm.3 1.3h2a10 10 0 0 0 .9 2.6 5 5 0 0 1-2.9-2.6zm2-5h-2a5 5 0 0 1 2.9-2.6c-.4.8-.7 1.7-.9 2.6zm2 7.5c-.5-.7-.9-1.6-1.1-2.5h2.2c-.2.9-.6 1.8-1.1 2.5zm1.4-3.8h-2.8a9 9 0 0 1 0-2.4h2.8a9 9 0 0 1 0 2.4zm.2 3.5c.4-.8.7-1.7.9-2.6h2a5 5 0 0 1-2.9 2.6zm1.1-3.8a11 11 0 0 0 0-2.4h2.1a5 5 0 0 1 0 2.4z"/></svg>
          <p class="contact__text">t.ashdale@solvarowindowsanddoors.com<br>solvarowindowsanddoors.com</p>
        </li>
      </ul>
    </div>
  </section>

</main>
</body>
</html>
```